Eye Catching Business Card for Optometrist

We've recently refreshed our logo and now we need a fresh and bold look for our business cards. We provide progressive ways to improve people's vision and protect their eye health.

Use our new logo as guidance into the colors to use. As far as style goes, I love how bold and eye catching the card is for Lantern Works. Feel free to use your creative judgement.

Tagline: "Sharply focused on your sight."

pertinent info to include:

Dr. Martin Pruell
Optometrist

2857 Wilmarth Ridge Blvd #207
Harlow Bend, KS 66093
(555) 382-9017

marty@brindlecoveeyecare.example
www.brindlecoveeyecare.example

```html
<!DOCTYPE html>
<html lang="en">
<head>
<meta charset="utf-8">
<title>Brindle Cove Eye Care – Business Card</title>
<link href="https://fonts.googleapis.com/css2?family=Open+Sans:wght@400;600;700&display=swap" rel="stylesheet">
<style>
  :root {
    --stage: #2b2b2b;
    --card-dark: #171717;
    --card-light: #ebebea;
    --brand-red: #c7242c;
    --brand-brown: #5f5048;
    --brand-sand: #cdb99b;
    --ink: #4a3f38;
    --ink-soft: #5a504a;
    --rule: #6b625c;
  }
  * { margin: 0; padding: 0; box-sizing: border-box; }
  html, body { width: 1200px; height: 1000px; overflow: hidden; }
  body {
    background: var(--stage);
    font-family: "Open Sans", Arial, sans-serif;
    position: relative;
  }
  .card {
    position: absolute;
    left: 260px;
    width: 680px;
    height: 385px;
    border-radius: 22px;
    overflow: hidden;
  }
  .card--front { top: 85px; background: var(--card-dark); }
  .card--back { top: 530px; background: var(--card-light); }

  .brand-mark {
    position: absolute;
    background: var(--brand-red);
  }
  .brand-name {
    position: absolute;
    color: var(--brand-red);
    font-weight: 700;
    text-transform: uppercase;
    line-height: 1.1;
    text-align: center;
    white-space: nowrap;
  }

  /* front */
  .card--front .brand-mark { left: 295px; top: 55px; width: 90px; height: 90px; }
  .card--front .brand-name { left: 0; width: 680px; top: 210px; font-size: 32px; }
  .front-rule {
    position: absolute; left: 0; top: 322px; width: 100%; height: 5px;
    background: var(--brand-red);
  }
  .tagline-band {
    position: absolute; left: 0; top: 332px; width: 100%; height: 53px;
    background: var(--brand-brown);
    display: flex; align-items: center; justify-content: center;
  }
  .tagline {
    color: var(--brand-sand);
    font-weight: 700;
    font-size: 21px;
    text-transform: uppercase;
    letter-spacing: 0.2px;
  }

  /* back */
  .card--back .brand-mark { left: 140px; top: 80px; width: 80px; height: 80px; }
  .card--back .brand-name { left: 60px; width: 240px; top: 238px; font-size: 28px; }
  .divider {
    position: absolute; left: 310px; top: 88px; width: 2px; height: 228px;
    background: var(--rule);
  }
  .contact { position: absolute; left: 335px; top: 92px; }
  .person-name { font-size: 22px; font-weight: 700; color: var(--ink); letter-spacing: 0.3px; }
  .person-role { font-size: 14px; font-weight: 700; color: var(--brand-red); margin-top: 2px; }
  .contact-list { list-style: none; margin-top: 26px; }
  .contact-list li {
    display: flex; align-items: flex-start; gap: 10px;
    font-size: 16px; color: var(--ink-soft); line-height: 22px; height: 29px;
  }
  .contact-list li.address { margin-top: 14px; height: auto; }
  .contact-list svg { width: 14px; height: 14px; margin-top: 4px; flex: none; fill: var(--ink); }
</style>
</head>
<body>

<section class="card card--front">
  <div class="brand-mark"></div>
  <div class="brand-name">Brindle Cove<br>Eye Care</div>
  <div class="front-rule"></div>
  <div class="tagline-band"><p class="tagline">Sharply focused on your sight.</p></div>
</section>

<section class="card card--back">
  <div class="brand-mark"></div>
  <div class="brand-name">Brindle Cove<br>Eye Care</div>
  <div class="divider"></div>
  <div class="contact">
    <p class="person-name">DR. MARTIN PRUELL</p>
    <p class="person-role">OPTOMETRIST</p>
    <ul class="contact-list">
      <li>
        <svg viewBox="0 0 16 16" aria-hidden="true"><path d="M1 6c0-2 3-3 7-3s7 1 7 3v1h-4V6H5v1H1z M3 8h10l1 6H2z M8 9.5a2 2 0 1 0 0 4 2 2 0 0 0 0-4z"/></svg>
        <span>(555) 382-9017</span>
      </li>
      <li>
        <svg viewBox="0 0 16 16" aria-hidden="true"><path d="M1 3h14v10H1z M2 4l6 5 6-5" stroke="#ebebea" stroke-width="1.2"/></svg>
        <span>marty@brindlecoveeyecare.example</span>
      </li>
      <li>
        <svg viewBox="0 0 16 16" aria-hidden="true"><circle cx="8" cy="8" r="7"/><path d="M1 8h14M8 1c-3 3-3 11 0 14M8 1c3 3 3 11 0 14" stroke="#ebebea" stroke-width="1" fill="none"/></svg>
        <span>www.brindlecoveeyecare.example</span>
      </li>
      <li class="address">
        <svg viewBox="0 0 16 16" aria-hidden="true"><path d="M8 1a5 5 0 0 0-5 5c0 4 5 9 5 9s5-5 5-9a5 5 0 0 0-5-5zm0 3a2 2 0 1 1 0 4 2 2 0 0 1 0-4z"/></svg>
        <span>2857 Wilmarth Ridge Blvd #207<br>Harlow Bend, KS 66093</span>
      </li>
    </ul>
  </div>
</section>

</body>
</html>
```